Design for online reviews widget

Attached is a wireframe of a widget we need designing to display reviews on websites from multiple sources. We need this provided at 3 different sizes including full screen, contained (like the wireframe) and mobile.
You have completely free rein on the styling.
The only elements that should remain untouched are the blue stars (https://www.filquarry.net/s/8vtmwp2291zq4h/kv%20stars.ai?dl=0) and powered by logo at the bottom.
Ignore the menu at the top of the wireframe, this is just from the website the widget will be placed on.
Businesses

```html
<!DOCTYPE html>
<html lang="en">
<head>
<meta charset="utf-8">
<title>Reviews widget</title>
<link href="https://fonts.googleapis.com/css2?family=Roboto:wght@400;500;700&display=swap" rel="stylesheet">
<style>
:root{
  --page:#1c2a33;
  --panel:#ffffff;
  --ink:#1f1f1f;
  --body:#5c5c5c;
  --line:#e2e2e2;
  --tile:#f7f7f7;
  --brand-blue:#35b6ea;
  --green:#5b9a22;
  --button:#5a9a2a;
  --orange:#f59a0c;
  --gold:#f8d21a;
  --score:#0f4f9c;
}
*{box-sizing:border-box;margin:0;padding:0}
html,body{width:807px;height:1200px;overflow:hidden}
body{background:var(--page);font-family:"Roboto",sans-serif;position:relative}
.panel{position:absolute;left:53px;top:58px;width:701px;height:1085px;background:var(--panel)}
.score-stars{position:absolute;left:279px;top:33px;display:flex;gap:4px}
.score-stars svg{width:26px;height:26px}
.score-title{position:absolute;left:0;width:701px;top:71px;text-align:center;font-size:15px;font-weight:400;color:var(--ink)}
.filter{position:absolute;left:568px;top:83px;width:112px;height:29px;border:1.3px solid #222;border-radius:6px;
  font-size:10.5px;color:var(--ink);display:flex;align-items:center;justify-content:space-between;padding:0 10px}
.filter svg{width:8px;height:5px}
.card{position:absolute;left:22px;width:657px;height:172px;border:1px solid #e6e6e6;border-radius:4px;
  box-shadow:0 1px 4px rgba(0,0,0,.08);background:#fff}
.source{position:absolute;left:8px;top:10px;width:147px;height:151px;background:var(--tile);border:1px solid #e4e4e4;border-radius:4px;
  display:flex;flex-direction:column;align-items:center;justify-content:center;gap:8px}
.source-name{font-size:17px;font-weight:500;color:#333}
.rating-ring{width:74px;height:74px;border-radius:50%;border:5px solid var(--score);display:flex;align-items:center;justify-content:center;
  font-size:18px;font-weight:700;color:var(--score)}
.gold-stars{display:flex;gap:1px}
.gold-stars svg{width:21px;height:21px;fill:var(--gold)}
.content{position:absolute;left:178px;top:18px;width:456px}
.review-title{font-size:14px;font-weight:500;color:var(--ink);white-space:nowrap}
.review-body{margin-top:13px;font-size:8.9px;letter-spacing:-0.15px;line-height:17.3px;color:var(--body);text-align:justify;hyphens:auto}
.review-body b{color:#333;font-weight:500}
.divider{position:absolute;left:172px;right:0;top:128px;border-top:1px solid var(--line)}
.meta{position:absolute;left:178px;top:142px;font-size:10.5px;color:var(--green);font-weight:500;display:flex;gap:30px}
.mini-stars{position:absolute;right:32px;top:145px;display:flex;gap:1px}
.mini-stars svg{width:11px;height:11px;fill:var(--orange)}
.load-more{position:absolute;left:280px;top:929px;width:141px;height:41px;border-radius:21px;background:var(--button);
  color:#fff;font-size:15px;display:flex;align-items:center;justify-content:center}
.powered{position:absolute;left:515px;top:1008px;display:flex;align-items:center;gap:6px}
.powered-mark{width:40px;height:40px;border-radius:50%;background:var(--brand-blue)}
.powered-text{font-size:11.5px;color:var(--ink);line-height:1.3}
.powered-text strong{display:block;font-size:18px;font-weight:700}
</style>
</head>
<body>
<svg width="0" height="0" style="position:absolute">
  <defs>
    <symbol id="star" viewBox="0 0 24 24"><path d="M12 2l2.9 6.3 6.9.7-5.2 4.6 1.5 6.8L12 16.9 5.9 20.4l1.5-6.8L2.2 9l6.9-.7z"/></symbol>
    <symbol id="badge" viewBox="0 0 26 26"><circle cx="13" cy="13" r="12.5" fill="#35b6ea"/><path fill="#fff" d="M13 5.5l2.2 4.7 5.1.6-3.8 3.4 1.1 5.1L13 16.7l-4.6 2.6 1.1-5.1-3.8-3.4 5.1-.6z"/></symbol>
  </defs>
</svg>

<main class="panel">
  <div class="score-stars">
    <svg><use href="#badge"/></svg><svg><use href="#badge"/></svg><svg><use href="#badge"/></svg><svg><use href="#badge"/></svg><svg><use href="#badge"/></svg>
  </div>
  <h1 class="score-title">Combined Review Score 4.3 out of 5</h1>
  <div class="filter">Filter Results <svg viewBox="0 0 8 5"><path d="M0 0h8L4 5z" fill="#111"/></svg></div>

  <article class="card" style="top:133px">
    <div class="source"><span class="source-name">TradeScore</span><div class="rating-ring">9.77</div></div>
    <div class="content">
      <h2 class="review-title">Front door with windows each side and side window</h2>
      <p class="review-body">This is the second time we have used keystone home improvements , and the service is amazing! Martin came round several times as we keep changing our minds and he was so helpful and gave us good advice, and the guys who do the fitting are efficient and tidy . I’ve got to say the end result is amazing and I have recommended to many of friends . Thanks Keystone <b>Reliablity: 9.38 Courtesy: 10 Tidiness: 9.84 Workmanship: 10</b></p>
    </div>
    <div class="divider"></div>
    <div class="meta"><span>Verified 28th September 2021</span><span>|</span><span>Located in Fernhollow</span></div>
    <div class="mini-stars"><svg><use href="#star"/></svg><svg><use href="#star"/></svg><svg><use href="#star"/></svg><svg><use href="#star"/></svg><svg><use href="#star"/></svg></div>
  </article>

  <article class="card" style="top:331px">
    <div class="source"><span class="source-name">Searchly</span>
      <div class="gold-stars"><svg><use href="#star"/></svg><svg><use href="#star"/></svg><svg><use href="#star"/></svg><svg><use href="#star"/></svg><svg><use href="#star"/></svg></div></div>
    <div class="content">
      <h2 class="review-title">Positive: Professionalism, Quality, Value</h2>
      <p class="review-body">The team did a good job of replacing a large feature window spanning two floors, as well as the others in my property. They’re a professional group who were willing to work out solutions to any problem, especially com&shy;pared to other companies. Prices are fair, and my new UPVC windows look great. Special thanks to Derek for being so accommodating and for the good communication throughout. <b>Service: Window installation</b></p>
    </div>
    <div class="divider"></div>
    <div class="meta"><span>11 months ago by Helen Carver</span></div>
    <div class="mini-stars"><svg><use href="#star"/></svg><svg><use href="#star"/></svg><svg><use href="#star"/></svg><svg><use href="#star"/></svg><svg><use href="#star"/></svg></div>
  </article>

  <article class="card" style="top:530px">
    <div class="source"><span class="source-name">Listwell</span>
      <div class="gold-stars"><svg><use href="#star"/></svg><svg><use href="#star"/></svg><svg><use href="#star"/></svg><svg><use href="#star"/></svg><svg><use href="#star"/></svg></div></div>
    <div class="content">
      <h2 class="review-title">Brilliant all round professional, friendly service.</h2>
      <p class="review-body">This home run friendly business was a real pleasure to deal with. From the professional, no pressure quote, nothing was too much trouble to ensure everything is as required for your needs with the quote and fitting. The workmanship and double glazing being fitted was brilliant and my home/outdoors was left tidy and clean leaving this company, such a brilliant service from great hardworking people that care about their service.</p>
    </div>
    <div class="divider"></div>
    <div class="meta"><span>13 Feb 2018 by GreenChair42</span></div>
    <div class="mini-stars"><svg><use href="#star"/></svg><svg><use href="#star"/></svg><svg><use href="#star"/></svg><svg><use href="#star"/></svg><svg><use href="#star"/></svg></div>
  </article>

  <article class="card" style="top:728px">
    <div class="source"><span class="source-name">RevueHub</span>
      <div class="gold-stars"><svg><use href="#star"/></svg><svg><use href="#star"/></svg><svg><use href="#star"/></svg><svg><use href="#star"/></svg><svg><use href="#star"/></svg></div></div>
    <div class="content">
      <h2 class="review-title">Front door with windows each side and side window</h2>
      <p class="review-body">This is the second time we have used keystone home improvements , and the service is amazing! Martin came round several times as we keep changing our minds and he was so helpful and gave us good advice, and the guys who do the fitting are efficient and tidy . I’ve got to say the end result is amazing and I have recommended to many of friends . Thanks Keystone</p>
    </div>
    <div class="divider"></div>
    <div class="meta"><span>13 Feb 2018 by Priya</span></div>
    <div class="mini-stars"><svg><use href="#star"/></svg><svg><use href="#star"/></svg><svg><use href="#star"/></svg><svg><use href="#star"/></svg><svg><use href="#star"/></svg></div>
  </article>

  <div class="load-more">Load More</div>

  <div class="powered">
    <span class="powered-mark"></span>
    <div class="powered-text">Powered by<strong>ReviewKnit</strong></div>
  </div>
</main>
</body>
</html>
```